Creative Landscape Architecture Company Needs a Creative Business Card Design

Marsh and Partners, Inc. is a landscape architecture (LA) company started in 1997 in Austin, TX. We work on large commerical projects all around the U.S. and provide land planning, site planning, landscape design and architectural renderings.

We don't want this card to look like a LA firm's business card. We are looking for a business card design that is edgy and cool to reflect the more artistic and creative side of our company. We would like our clients to think "now there's a business card unlike any other LA that I've seen before."

We would like it to be in standard 2"x3.5" format. Double sided. Full color ok. Our company logo is attached. We like the logo but would not be adverse to any variations you would like to make to it. Feel free to change it up. Typically the logo has been a light saturated orange color but its not necessary that you stick with it.

Requirements
Must have
• 1. Company name
2. individuals name
3. email address
4. cell number
5. office number
6. website: www.marshandpartners-demo.net
7. Business address
Nice to have
• Can add (but not necessary)
Personal titles such as "president" or "registered landscape architect"

```html
<!DOCTYPE html>
<html lang="en">
<head>
<meta charset="utf-8">
<title>Marsh and Partners, Inc. — Business Card</title>
<link rel="stylesheet" href="https://fonts.googleapis.com/css2?family=Source+Sans+3:wght@400;600;700&display=swap">
<style>
  :root {
    --page: #ebe8e4;
    --card-light: #d9dadc;
    --card-mid: #b7b9bc;
    --panel: #050505;
    --accent: #d9891f;
    --accent-edge: #c9781a;
    --text-light: #ffffff;
    --label: #d28a2a;
  }
  * { margin: 0; padding: 0; box-sizing: border-box; }
  html, body {
    width: 1200px;
    height: 880px;
    overflow: hidden;
    background: var(--page);
    font-family: "Source Sans 3", "Myriad Pro", Arial, sans-serif;
  }
  .stage {
    width: 1200px;
    height: 880px;
    display: flex;
    flex-direction: column;
    align-items: center;
    justify-content: center;
    gap: 40px;
  }
  .card {
    position: relative;
    width: 660px;
    height: 377px;
    overflow: hidden;
    box-shadow: 0 6px 18px rgba(0, 0, 0, 0.18);
  }
  .card-pattern {
    position: absolute;
    inset: 0;
    background:
      radial-gradient(ellipse at 30% 35%, var(--card-light) 0%, transparent 55%),
      radial-gradient(ellipse at 75% 70%, var(--card-light) 0%, transparent 50%),
      linear-gradient(135deg, var(--card-mid) 0%, #c8c9cc 50%, var(--card-mid) 100%);
  }

  /* Contact side */
  .contact-panel {
    position: absolute;
    left: 52px;
    top: 42px;
    width: 560px;
    height: 296px;
    background: var(--panel);
    border-left: 6px solid var(--accent-edge);
    padding: 26px 0 0 38px;
    color: var(--text-light);
  }
  .person {
    display: flex;
    align-items: baseline;
    gap: 36px;
    margin-left: 34px;
    margin-bottom: 22px;
  }
  .person-name {
    color: var(--accent);
    font-weight: 700;
    font-size: 28px;
    letter-spacing: 0.2px;
  }
  .person-title {
    font-size: 16px;
    font-weight: 400;
  }
  .contact-list {
    display: grid;
    grid-template-columns: 72px 16px auto;
    row-gap: 3px;
    font-size: 17px;
    line-height: 1.25;
  }
  .contact-label {
    color: var(--label);
    text-align: right;
  }
  .contact-sep {
    color: var(--text-light);
    text-align: center;
  }
  .contact-value { color: var(--text-light); }

  /* Company side */
  .company-band {
    position: absolute;
    left: 180px;
    top: 128px;
    width: 430px;
    height: 96px;
    background: var(--panel);
    border-left: 6px solid var(--accent-edge);
    display: flex;
    align-items: center;
    justify-content: center;
  }
  .company-name {
    color: var(--text-light);
    font-weight: 700;
    font-size: 33px;
    letter-spacing: 0.2px;
  }
</style>
</head>
<body>
  <main class="stage">
    <section class="card card-contact">
      <div class="card-pattern" role="img" aria-label="Large pale grey leaf ornament pattern covering the card"></div>
      <div class="contact-panel">
        <div class="person">
          <span class="person-name">Daniel Reyes</span>
          <span class="person-title">| manager</span>
        </div>
        <div class="contact-list">
          <span class="contact-label">Office</span><span class="contact-sep">:</span><span class="contact-value">+0 555 010 2468</span>
          <span class="contact-label">Cell</span><span class="contact-sep">:</span><span class="contact-value">+0 555 014 7731</span>
          <span class="contact-label">E-mail</span><span class="contact-sep">:</span><span class="contact-value">daniel@marshandpartners-demo.net</span>
          <span class="contact-label">Website</span><span class="contact-sep">:</span><span class="contact-value">www.marshandpartners-demo.net</span>
          <span class="contact-label">Address</span><span class="contact-sep">:</span><span class="contact-value">4410 Cedar Bend, B118-240</span>
          <span class="contact-label"></span><span class="contact-sep"></span><span class="contact-value">Austin, Texas 78700</span>
        </div>
      </div>
    </section>

    <section class="card card-company">
      <div class="card-pattern" role="img" aria-label="Large pale grey leaf ornament pattern covering the card"></div>
      <div class="company-band">
        <span class="company-name">Marsh and Partners, Inc.</span>
      </div>
    </section>
  </main>
</body>
</html>
```